Vorel constructions

We are predominantly a residential home builder based in Melbourne, Victoria Australia. We construct houses, apartments, townhouses, multi-unit developments.

The name of the company is "Vorel Constructions"
My company believes in building unique construction projects mainly residential homes. The target customers are upmarket Melbourne residents/investors.

I want the brand name "Vorel" to be part of the logo. There's no need to put the word construction in the logo at this stage.

I would also like some ideas for a slogan e.g. "Just build it." or "We build quality homes." But I would like something unique and different for a slogan not the same old cliche.

vorelconstructions.example.com.au
e: tmelo@vorelconstructions.example.com.au
M: 0417305862
Address: 8/3 Fenwick Lane Clayton VIC 3168

Director:Mr Dinesh Malarkodiyan

```html
<!DOCTYPE html>
<html lang="en">
<head>
<meta charset="utf-8">
<title>Vorel Constructions – Business Card</title>
<link rel="stylesheet" href="https://fonts.googleapis.com/css2?family=Roboto+Condensed:ital,wght@0,400;0,700;1,400&display=swap">
<style>
  :root {
    --backdrop: #e9e6e1;
    --card: #f4f4f5;
    --navy: #10306c;
    --sky: #2aa8e0;
    --sky-soft: #9fd7f1;
    --white: #ffffff;
  }
  html, body {
    margin: 0;
    width: 1200px;
    height: 900px;
    overflow: hidden;
    background: var(--backdrop);
    font-family: "Roboto Condensed", "Arial Narrow", sans-serif;
  }
  .business-card {
    position: absolute;
    left: 100px;
    top: 165px;
    width: 1000px;
    height: 571px;
    background: var(--card);
    overflow: hidden;
    box-shadow: 0 6px 24px rgba(0,0,0,0.15);
  }
  .brand-name {
    position: absolute;
    left: 58px;
    top: 34px;
    margin: 0;
    font-size: 58px;
    font-weight: 400;
    color: var(--sky);
    letter-spacing: 1px;
    line-height: 1;
  }
  .contact-list {
    position: absolute;
    left: 70px;
    top: 140px;
    margin: 0;
    padding: 0;
    list-style: none;
  }
  .contact-item {
    display: flex;
    align-items: center;
    height: 38px;
    font-size: 27px;
    color: var(--navy);
  }
  .contact-icon {
    width: 22px;
    height: 22px;
    margin-right: 22px;
    fill: var(--navy);
  }
  .person {
    position: absolute;
    right: 64px;
    top: 170px;
    text-align: right;
    color: var(--navy);
  }
  .person-name {
    margin: 0;
    font-size: 32px;
    font-weight: 400;
  }
  .person-role {
    margin: 2px 0 0;
    font-size: 24px;
  }
  .footer-band {
    position: absolute;
    left: 0;
    top: 0;
    width: 1000px;
    height: 571px;
  }
  .slogan {
    position: absolute;
    right: 64px;
    bottom: 44px;
    margin: 0;
    font-size: 24px;
    font-style: italic;
    color: var(--white);
  }
</style>
</head>
<body>
<main class="business-card">
  <svg class="footer-band" viewBox="0 0 1000 571" aria-hidden="false">
    <defs>
      <linearGradient id="skyline-tone" x1="0" y1="0" x2="0" y2="1">
        <stop offset="0" stop-color="#2aa8e0"/>
        <stop offset="1" stop-color="#9fd7f1"/>
      </linearGradient>
    </defs>
    <path d="M0,425 C250,380 600,352 1000,342 L1000,571 L0,571 Z" fill="var(--sky)"/>
    <path d="M0,448 C260,408 620,380 1000,372 L1000,571 L0,571 Z" fill="var(--navy)"/>
    <rect x="560" y="300" width="320" height="118" fill="url(#skyline-tone)" role="img" aria-label="Stylised city skyline of apartment towers"/>
  </svg>

  <h1 class="brand-name">Vorel</h1>

  <ul class="contact-list">
    <li class="contact-item">
      <svg class="contact-icon" viewBox="0 0 24 24"><path d="M6.6 10.8a15 15 0 0 0 6.6 6.6l2.2-2.2c.3-.3.7-.4 1-.2 1.1.4 2.3.6 3.6.6.6 0 1 .4 1 1V20c0 .6-.4 1-1 1A17 17 0 0 1 3 4c0-.6.4-1 1-1h3.5c.6 0 1 .4 1 1 0 1.3.2 2.5.6 3.6.1.3 0 .7-.2 1z"/></svg>
      08 7041 3350
    </li>
    <li class="contact-item">
      <svg class="contact-icon" viewBox="0 0 24 24"><path d="M6 2h10v6H6zM3 9h18v9h-3v4H6v-4H3zm5 7v4h8v-4z"/></svg>
      08 7041 3361
    </li>
    <li class="contact-item">
      <svg class="contact-icon" viewBox="0 0 24 24"><path d="M7 1h10c1 0 2 1 2 2v18c0 1-1 2-2 2H7c-1 0-2-1-2-2V3c0-1 1-2 2-2zm0 3v14h10V4z"/></svg>
      0417305862
    </li>
    <li class="contact-item">
      <svg class="contact-icon" viewBox="0 0 24 24"><path d="M2 5h20v14H2zm2 2v1l8 5 8-5V7l-8 5z"/></svg>
      tmelo@vorelconstructions.example.com.au
    </li>
    <li class="contact-item">
      <svg class="contact-icon" viewBox="0 0 24 24"><circle cx="12" cy="12" r="10"/></svg>
      vorelconstructions.example.com.au
    </li>
  </ul>

  <div class="person">
    <p class="person-name">Dinesh Malarkodiyan</p>
    <p class="person-role">Director</p>
  </div>

  <p class="slogan">Just build your dream home!</p>
</main>
</body>
</html>
```